TRVesper Labels*

We are in the cannabis industry selling Cannabis products in a 1oz jar, 3oz jar and 7 oz jars. we have pre-rolls too.

We need various sizes logo label stickers for small jars and tubes. I need label sticker designs for some 1"x2", 2"x3", 2"x2" stickers logo. See attached for examples.

I'm attaching some samples for you to look at and see if you can design something in similar.

Attached is our Logo designed my PixelHarbor Project Design #: 58402936
Our Slogan is:

“Staying Passionate and motivated by high quality cannabis”

For any questions please do not hesitate to ask. Thank you

Target Market(s)

general comsumers

Industry/Entity Type

Cannabis

Font styles to use
Decorative

Colors
abd037
f36f22
f78f20
ffc41a

Requirements
Must have
• Warning: This product may be unlawful outside of the State of Washington. This soil grown product has intoxicating effects and my be habit forming. Smoking is hazardous to your health. There may be health risks associated with the consumption of this product. Marijuana can impair concentration, coordination and judgement. Do not operate a vehicle or machinery under the influence of this drug. Should not be use by women that are pregnant or breast feeding. For use only by adults twenty-one and older. Keep out reach of children.
Nice to have
• Small text box for cannabis name and strain type
• Marketing: Check Us Out!
• www.TRVesperLLC-example.com
• TRVesperLLC@mailbox-example.com
• Chatterbook TRVesper LLC

```html
<!DOCTYPE html>
<html lang="en">
<head>
<meta charset="UTF-8">
<title>TRVesper Cannabis Label</title>
<link rel="stylesheet" href="https://fonts.googleapis.com/css2?family=Montserrat:wght@500;600&family=Questrial&display=swap">
<style>
  :root {
    --leaf-bg: #d3e89b;
    --leaf-bg-light: #dcefa8;
    --leaf-bg-deep: #c6e08a;
    --brand-green: #a6cc3a;
    --leaf-dark: #1f7a3c;
    --ink: #363636;
    --paper: #ffffff;
  }
  * { margin: 0; padding: 0; box-sizing: border-box; }
  html, body { width: 800px; height: 1200px; overflow: hidden; }
  body { font-family: "Montserrat", sans-serif; color: var(--ink); }

  .label {
    position: relative;
    width: 800px;
    height: 1200px;
    overflow: hidden;
    background: var(--leaf-bg);
  }
  .label__pattern {
    position: absolute;
    inset: 0;
    background: radial-gradient(circle at 50% 45%, var(--leaf-bg-light) 0%, var(--leaf-bg) 55%, var(--leaf-bg-deep) 100%);
  }

  .brand-card {
    position: absolute;
    left: 100px;
    top: 0;
    width: 638px;
    height: 400px;
    background: linear-gradient(180deg, #f3f8e4 0%, var(--paper) 30%);
    border-radius: 0 0 40px 40px;
    box-shadow: 0 10px 22px rgba(60, 80, 20, 0.25);
  }
  .brand-card__mark {
    position: absolute;
    left: 50%;
    top: 80px;
    width: 120px;
    height: 120px;
    margin-left: -60px;
    border-radius: 50%;
    background: var(--brand-green);
  }
  .brand-card__name {
    position: absolute;
    left: 0;
    right: 0;
    top: 296px;
    text-align: center;
    font-family: "Questrial", sans-serif;
    font-size: 80px;
    line-height: 1;
    color: var(--brand-green);
  }

  .product-word {
    position: absolute;
    left: 86px;
    top: 660px;
    font-family: "Questrial", sans-serif;
    font-size: 150px;
    font-weight: 400;
    line-height: 1;
    letter-spacing: 1px;
    color: var(--ink);
  }
  .product-leaf {
    position: absolute;
    left: 560px;
    top: 552px;
    width: 158px;
    height: 140px;
    border-radius: 50% 50% 40% 40%;
    background: radial-gradient(circle, #7fbf6a 0%, var(--leaf-dark) 75%);
    opacity: 0.55;
  }

  .slogan-band {
    position: absolute;
    left: 0;
    top: 810px;
    width: 791px;
    height: 88px;
    background: var(--paper);
    display: flex;
    align-items: center;
    justify-content: center;
  }
  .slogan {
    text-align: center;
    font-weight: 600;
    font-size: 29px;
    line-height: 38px;
    letter-spacing: 0.2px;
    color: #2e2e2e;
    white-space: nowrap;
  }

  .contacts {
    position: absolute;
    left: 383px;
    top: 1032px;
    list-style: none;
  }
  .contacts__item {
    display: flex;
    align-items: center;
    height: 50px;
    font-weight: 500;
    font-size: 18px;
    white-space: nowrap;
    color: var(--ink);
  }
  .contacts__icon {
    width: 26px;
    height: 26px;
    margin-right: 23px;
    flex: none;
  }
  .contacts__dot {
    width: 14px;
    height: 14px;
    margin: 0 29px 0 6px;
    border-radius: 50%;
    background: var(--ink);
    flex: none;
  }
</style>
</head>
<body>
<main class="label">
  <div class="label__pattern" role="img" aria-label="Light green background with a faint geometric line pattern"></div>

  <header class="brand-card">
    <div class="brand-card__mark"></div>
    <div class="brand-card__name">TRVesper</div>
  </header>

  <div class="product-leaf" role="img" aria-label="Outlined cannabis leaf ornament above the word cannabis"></div>
  <h1 class="product-word">cannabis</h1>

  <div class="slogan-band">
    <p class="slogan">STAYING PASSIONATE &amp; MOTIVATED BY<br>HIGH QUALITY CANNABIS</p>
  </div>

  <ul class="contacts">
    <li class="contacts__item">
      <svg class="contacts__icon" viewBox="0 0 26 26" fill="none" stroke="#4a4a4a" stroke-width="1.6">
        <circle cx="13" cy="13" r="11"/>
        <ellipse cx="13" cy="13" rx="5" ry="11"/>
        <line x1="2" y1="13" x2="24" y2="13"/>
        <path d="M4 7.5h18M4 18.5h18"/>
      </svg>
      www.TRVesperLLC-example.com
    </li>
    <li class="contacts__item">
      <svg class="contacts__icon" viewBox="0 0 26 26" fill="none" stroke="#4a4a4a" stroke-width="1.6">
        <rect x="2" y="6" width="22" height="15"/>
        <path d="M2 6l11 9 11-9M2 21l8-7M24 21l-8-7"/>
      </svg>
      TRVesperLLC@mailbox-example.com
    </li>
    <li class="contacts__item">
      <span class="contacts__dot"></span>
      TRVesper LLC
    </li>
  </ul>
</main>
</body>
</html>
```